Saltmarsh Motocross Club. Sports club.

We are a family orientated Motocross Club in Abu Dhabi. We have 3 motocross tracks, Intermediate Track, Junior rack and E-track. We also have a School(Academy) and maintenance facility that caters for all motorbike services. We have a BBQ area with a 20x70 meter pool after a hot day of riding. We are busy adding a restaurant and bar in the next few weeks. We host 6 Club races in the season as well as the Crescent Ridge Championship. Therefore we will need a race calendar as well as race results page. The school have a dedicated school facility with bike rental, bike show room, gear rental and small shop. We have instructors that instruct kids from 4 years old to professional riders.

Target Market(s)

Motocross riders, kids from 4 years

Industry/Entity Type

extreme sports, motorsports motocross

Coding

Coded - Design and coding required

Number of Pages Required

5+ page

Font styles to use
Sans Serif

Colors

Designer to choose colors to be used in the design.

Requirements
Must have
• User Friendly, Easy to update, Calendar , online payment, race results, academy, facilities,
Nice to have
• Just an update it has to have a calendar with sides that shows whats happening on the day. We also need at the top of page the "open hours", " a next event" button, our partners button at the bottom of page a "News Page" "testimonials" with all the necessary links, social medial, address, contact details, etc.
Should not have
• no cartoons or any clipart please just photos

```html
<!DOCTYPE html>
<html lang="en">
<head>
<meta charset="utf-8">
<title>Saltmarsh Motocross Club</title>
<link href="https://fonts.googleapis.com/css2?family=Russo+One&family=Barlow+Condensed:wght@700&family=Montserrat:wght@400;500;600;700&display=swap" rel="stylesheet">
<style>
:root{
  --red:#d3121c;
  --red-dark:#8f0a10;
  --ink:#141414;
  --black:#050505;
  --grey-bg:#e6e6e6;
  --card-dark:#2a2a2a;
  --text:#333;
  --muted:#777;
  --white:#fff;
}
*{box-sizing:border-box;margin:0;padding:0}
html,body{width:1200px;height:4988px;overflow:hidden}
body{font-family:'Montserrat',Arial,sans-serif;color:var(--text);background:var(--white);position:relative}
.title{font-family:'Russo One',Arial,sans-serif;font-weight:400;color:var(--ink);text-transform:uppercase}
.title em{font-style:normal;color:var(--red)}
.bar{display:block;width:48px;height:4px;background:var(--red);margin:10px auto 0}
.photo{position:absolute}
.btn-outline{display:inline-block;border:2px solid var(--red);color:var(--red);font-weight:700;font-size:13px;text-transform:uppercase;border-radius:30px}

/* top bar */
.topbar{height:33px;background:var(--red);color:var(--white);font-size:11px;font-weight:600;position:relative}
.topbar .hours{position:absolute;left:352px;top:10px}
.topbar .phone{position:absolute;left:826px;top:9px;font-size:13px}
.topbar .next{position:absolute;right:110px;top:0;height:33px;width:110px;background:#3a0406;text-align:center;line-height:33px;font-size:11px}
.topbar svg{vertical-align:-3px;margin-right:4px}

/* nav */
.nav{height:97px;position:relative;background:var(--white)}
.brand{position:absolute;left:110px;top:30px;font-family:'Russo One',sans-serif;font-size:40px;color:var(--red);display:flex;align-items:center;gap:10px}
.brand i{width:14px;height:14px;background:var(--red);display:block}
.menu{position:absolute;left:0;top:44px;width:960px;height:30px;font-size:11px;font-weight:700;color:var(--ink)}
.menu span{position:absolute;top:0;white-space:nowrap}
.menu .active{color:var(--red);border-bottom:2px solid var(--red);padding-bottom:8px}
.partner-btn{position:absolute;left:965px;top:37px;width:120px;height:34px;border-radius:20px;background:var(--red);color:var(--white);font-size:11px;font-weight:700;text-align:center;line-height:34px}

/* hero */
.hero{position:relative;height:542px;background:linear-gradient(100deg,#5a3d22 0%,#8a6a45 35%,#3c3a44 65%,#2a2c3a 100%)}
.hero-kicker{position:absolute;left:444px;top:131px;width:332px;height:33px;background:rgba(20,20,20,.8);color:var(--white);font-size:26px;letter-spacing:4px;text-align:center;line-height:33px;font-weight:500}
.hero-title{position:absolute;left:0;right:0;top:172px;text-align:center;font-family:'Barlow Condensed',sans-serif;font-size:78px;line-height:68px;color:var(--white);text-transform:uppercase}
.hero-btn{position:absolute;left:540px;top:328px;width:170px;height:42px;border:2px solid var(--white);border-radius:24px;color:var(--white);text-align:center;line-height:38px;font-size:15px;font-weight:600}

.tiles{position:absolute;top:584px;left:0;width:1200px;height:273px;z-index:2}
.tile{position:absolute;color:var(--white);text-align:center;padding:0 32px}
.tile h3{font-family:'Russo One',sans-serif;font-weight:400;font-size:20px;margin-bottom:12px}
.tile p{font-size:10px;font-weight:600;line-height:15px}
.tile .chev{display:block;margin:12px auto 0}
.tile-dark{left:118px;top:36px;width:308px;height:212px;background:linear-gradient(135deg,#3a3a3a,#1e1e1e);padding-top:56px}
.tile-red{left:426px;top:0;width:358px;height:273px;background:linear-gradient(135deg,#e41a22,#a80c12);padding-top:80px;box-shadow:0 0 0 10px rgba(211,18,28,.35) inset}
.tile-grey{left:784px;top:36px;width:300px;height:212px;background:linear-gradient(135deg,#9a9a9a,#6b6b6b);padding-top:56px}

/* about */
.about{position:relative;height:789px}
.ring{position:absolute;left:106px;top:241px}
.about-photo{left:152px;top:287px;width:392px;height:392px;border-radius:50%;background:radial-gradient(circle at 50% 40%,#8fa2bf,#c9a27a 70%,#8b6a45)}
.about-text{position:absolute;left:631px;top:300px;width:452px}
.about-text .title{font-size:46px;line-height:52px}
.about-text .bar{margin:6px 0 0}
.about-text p{font-size:14px;line-height:22px;margin-top:24px;color:#444}
.about-text p + p{margin-top:20px}
.about-text .btn-outline{margin-top:24px;width:170px;height:46px;line-height:42px;text-align:center}

/* featured events */
.featured{position:relative;height:571px;background:var(--grey-bg)}
.featured .title{text-align:center;font-size:33px;padding-top:40px}
.calendar{position:absolute;left:126px;top:139px;width:396px}
.cal-head{height:50px;background:var(--white);display:flex;justify-content:center;align-items:center;gap:50px;font-size:20px;color:var(--ink);font-weight:500}
.calendar table{width:100%;border-collapse:collapse;table-layout:fixed}
.calendar th{background:var(--red);color:var(--white);font-size:12px;font-weight:600;height:34px}
.calendar td{background:#3a3a3a;color:var(--white);text-align:center;font-size:17px;height:47px;border:1px solid #555}
.calendar td.today{background:var(--red)}
.ev-list{position:absolute;left:573px;top:180px;width:520px}
.ev{display:flex;gap:18px;height:122px}
.ev .thumb{width:100px;height:100px;border-radius:50%;flex:none;box-shadow:0 0 0 3px var(--white)}
.ev h4{font-size:14px;font-weight:700;color:var(--ink);margin-top:6px}
.ev p{font-size:13px;line-height:21px;color:#444}

/* news */
.news{position:relative;height:542px;background:var(--black)}
.news .title{color:var(--white);text-align:center;font-size:33px;padding-top:52px}
.news-card{position:absolute;top:124px;width:313px;height:334px;background:#2b2b2b}
.news-card .pic{height:209px;position:relative}
.date{position:absolute;left:10px;bottom:8px;background:var(--red);color:var(--white);font-size:11px;font-weight:700;padding:4px 10px}
.news-card h4{font-size:14px;font-weight:600;color:var(--white);line-height:21px;padding:24px 26px 0}
.news-card .more{font-size:10px;font-weight:700;color:var(--white);padding:18px 26px 0}
.news-card .more b{color:var(--red)}

/* testimonials */
.testi{position:relative;height:445px}
.testi .title{text-align:center;font-size:33px;padding-top:48px}
.quote{position:absolute;top:158px;width:443px;height:196px;border:2px solid var(--red);text-align:center;padding:60px 30px 0;font-size:12px;line-height:19px;color:#444}
.quote .by{font-weight:700;color:var(--ink);margin-top:18px;display:block}
.avatar{position:absolute;top:-47px;left:176px;width:90px;height:90px;border-radius:50%;border:4px solid var(--white)}
.qmark{position:absolute;right:28px;bottom:14px}
.arrow{position:absolute;top:227px}

/* training */
.training{position:relative;height:499px;overflow:hidden;background:linear-gradient(110deg,#2c2926,#8b7a66)}
.train-bg{position:absolute;left:0;top:0}
.train-text{position:absolute;left:105px;top:110px;width:370px;color:var(--white)}
.train-text .title{color:var(--white);font-size:30px}
.train-text .bar{margin:14px 0 0;background:var(--white)}
.train-text p{font-size:12px;line-height:19px;margin-top:26px}
.train-text p + p{margin-top:20px}
.train-text .btn{display:inline-block;margin-top:26px;width:138px;height:36px;border:2px solid var(--white);color:var(--white);font-size:11px;font-weight:700;text-align:center;line-height:32px}

/* latest events */
.latest{position:relative;height:623px;background:var(--grey-bg)}
.latest .title{position:absolute;left:122px;top:50px;font-size:31px}
.latest .bar{position:absolute;left:122px;top:95px;margin:0}
.le-pic{position:absolute;top:139px;width:478px;height:330px}
.le-card{position:absolute;top:381px;width:426px;height:171px;background:var(--white);border-bottom:3px solid var(--red);padding:18px 35px 0}
.le-card .d{color:var(--red);font-size:12px;font-weight:700}
.le-card h4{font-size:17px;font-weight:700;color:var(--ink);text-transform:uppercase}
.le-card i{display:block;width:40px;height:3px;background:var(--red);margin:6px 0 10px}
.le-card p{font-size:11px;line-height:16px;color:#555}
.le-card span{display:inline-block;margin-top:14px;border:2px solid var(--red);color:var(--red);font-size:9px;font-weight:700;padding:6px 22px}

/* partners */
.partners{position:relative;height:474px}
.partners .title{text-align:center;font-size:33px;padding-top:54px}
.logos{position:absolute;left:110px;width:980px;display:flex;justify-content:space-between;align-items:center}
.logos span{display:block;background:#9a9a9a}

/* footer */
.footer{position:relative;height:373px;background:var(--black);color:var(--white)}
.f-brand{position:absolute;left:106px;top:82px;font-family:'Russo One',sans-serif;font-size:48px;color:var(--red);display:flex;align-items:center;gap:10px}
.f-brand i{width:16px;height:16px;background:var(--red);display:block}
.socials{position:absolute;left:118px;top:182px;display:flex;gap:8px}
.socials span{width:30px;height:30px;border-radius:50%;border:2px solid var(--white);background:var(--red)}
.f-col{position:absolute;top:60px}
.f-col h5{font-size:13px;font-weight:700;letter-spacing:.5px;margin-bottom:14px}
.f-nav{display:grid;grid-template-columns:122px 110px;row-gap:8px;font-size:10px}
.f-news p{font-size:8.5px;line-height:11px;color:#bbb;margin-bottom:12px}
.f-news p b{color:var(--white);display:block;font-size:9px}
.f-contact div{display:flex;gap:10px;align-items:center;font-size:10px;margin-bottom:16px;line-height:13px}
.f-contact .ic{width:26px;height:26px;border-radius:50%;background:var(--white);flex:none;display:flex;align-items:center;justify-content:center}
.vline{position:absolute;top:0;width:1px;height:300px;background:#2a2a2a}
.f-rule{position:absolute;left:60px;right:60px;top:292px;height:1px;background:#2a2a2a}
.copy{position:absolute;left:0;right:0;top:312px;text-align:center;font-size:9px;color:#aaa}
</style>
</head>
<body>

<header class="topbar">
  <span class="hours"><svg width="12" height="12" viewBox="0 0 12 12"><circle cx="6" cy="6" r="5" fill="none" stroke="#fff" stroke-width="1.4"/><path d="M6 3v3.2l2 1.3" stroke="#fff" stroke-width="1.2" fill="none"/></svg>OPEN HOURS: MON TO FRI: 10 AM TO 8 PM &nbsp;|&nbsp; SAT &amp; SUN: 9AM TO 5PM</span>
  <span class="phone"><svg width="16" height="16" viewBox="0 0 16 16"><circle cx="8" cy="8" r="8" fill="#fff"/><path d="M5.5 4.5l1.4 1.8-.8 1c.5 1 1.3 1.8 2.4 2.4l1-.8 1.8 1.4-.8 1.2c-2.6-.3-5.1-2.8-5.4-5.4z" fill="#d3121c"/></svg>(+971) 555 0142</span>
  <span class="next">NEXT EVENT ›</span>
</header>

<nav class="nav">
  <div class="brand"><i></i>SMC</div>
  <div class="menu">
    <span class="active" style="left:352px">ABOUT US</span><span style="left:456px">FEATURED EVENT</span><span style="left:603px">UPCOMING RACE</span><span style="left:748px">TESTIMONIALS</span><span style="left:871px">CONTACT</span>
  </div>
  <span class="partner-btn">OUR PARTNER</span>
</nav>

<section class="hero" role="img" aria-label="Two motocross riders jumping over a dusty track">
  <div class="hero-kicker">WELCOME TO SMC</div>
  <h1 class="hero-title">Saltmarsh<br>Moto Cross</h1>
  <span class="hero-btn">LEARN MORE</span>
</section>
<div class="tiles">
  <div class="tile tile-dark" role="img" aria-label="Rental bikes and riding gear">
    <h3>BIKE &amp; GEAR RENTAL</h3>
    <p>Lorem ipsum dolor sit amet, consectetur adipiscing elit, sed do eiusmod tempor incididunt ut labo</p>
    <svg class="chev" width="30" height="30" viewBox="0 0 30 30"><circle cx="15" cy="15" r="13" fill="none" stroke="#fff" stroke-width="1.5"/><path d="M10 13l5 5 5-5" stroke="#fff" stroke-width="1.8" fill="none"/></svg>
  </div>
  <div class="tile tile-red" role="img" aria-label="Rider on a motocross bike at a featured event">
    <h3>FEATURED EVENT</h3>
    <p>Lorem ipsum dolor sit amet, consectetur adipiscing elit, sed do eiusmod tempor incididunt ut labo</p>
    <svg class="chev" width="34" height="34" viewBox="0 0 30 30"><circle cx="15" cy="15" r="13" fill="none" stroke="#fff" stroke-width="1.5"/><path d="M10 13l5 5 5-5" stroke="#fff" stroke-width="1.8" fill="none"/></svg>
  </div>
  <div class="tile tile-grey" role="img" aria-label="Motocross bikes in the club shop">
    <h3>OUR SHOP</h3>
    <p>Lorem ipsum dolor sit amet, consectetur adipiscing elit, sed do eiusmod tempor incididunt ut labo</p>
    <svg class="chev" width="30" height="30" viewBox="0 0 30 30"><circle cx="15" cy="15" r="13" fill="none" stroke="#fff" stroke-width="1.5"/><path d="M10 13l5 5 5-5" stroke="#fff" stroke-width="1.8" fill="none"/></svg>
  </div>
</div>

<section class="about">
  <svg class="ring" width="484" height="484" viewBox="0 0 484 484"><circle cx="242" cy="242" r="238" fill="none" stroke="#999" stroke-width="1.5"/><circle cx="242" cy="242" r="230" fill="none" stroke="#bbb" stroke-width="1"/><circle cx="242" cy="242" r="222" fill="none" stroke="#999" stroke-width="1.5"/><path d="M120 440a230 230 0 0 0 150 40" stroke="#d3121c" stroke-width="3" fill="none"/></svg>
  <div class="photo about-photo" role="img" aria-label="Rider in pink gear jumping on a motocross bike"></div>
  <div class="about-text">
    <h2 class="title">About <em>SMC</em></h2>
    <span class="bar"></span>
    <p>Lorem ipsum dolor sit amet, consectetur adipiscing elit, sed do eiusmod tempor incididunt ut labore et dolore magna aliqua. Ut enim ad minim veniam, quis nostrud exercitation ullamco laboris nisi ut aliquip ex ea commodo consequat.</p>
    <p>Duis aute irure dolor in reprehenderit in voluptate velit esse cillum dolore eu fugiat nulla pariatur. Excepteur sintLorem ipsum dolor sit amet, consectetur adipiscing elit, sed do</p>
    <span class="btn-outline">LEARN MORE</span>
  </div>
</section>

<section class="featured">
  <h2 class="title">Featured <em>Events</em></h2>
  <span class="bar"></span>
  <div class="calendar">
    <div class="cal-head"><span style="color:#999">‹</span><span>JUN 2022</span><span style="color:#999">›</span></div>
    <table>
      <tr><th>MO</th><th>TU</th><th>WE</th><th>TH</th><th>FR</th><th>SA</th><th>SU</th></tr>
      <tr><td>1</td><td>2</td><td>3</td><td>3</td><td>5</td><td>6</td><td>7</td></tr>
      <tr><td>8</td><td>9</td><td>10</td><td>11</td><td class="today">12</td><td>13</td><td>14</td></tr>
      <tr><td>15</td><td>16</td><td>17</td><td>18</td><td>19</td><td>20</td><td>21</td></tr>
      <tr><td>22</td><td>23</td><td>24</td><td>25</td><td>26</td><td>27</td><td>28</td></tr>
      <tr><td></td><td>30</td><td>31</td><td></td><td></td><td></td><td></td></tr>
    </table>
  </div>
  <div class="ev-list">
    <div class="ev"><div class="thumb" role="img" aria-label="Rider on a blue motocross bike" style="background:radial-gradient(#6d7ea0,#3a3f55)"></div><div><h4>Lorem ipsum dolor sit amet consectetur</h4><p>elit, sed do eiusmod tempor incididunt ut labore et dolore magna aliqua. Ut enim ad minim</p></div></div>
    <div class="ev"><div class="thumb" role="img" aria-label="Rider in purple gear cornering" style="background:radial-gradient(#9a7fb0,#6b5a3e)"></div><div><h4>Ut enim ad minima veniam</h4><p>elit, sed do eiusmod tempor incididunt ut labore et dolore magna aliqua. Ut enim ad minim veniam</p></div></div>
    <div class="ev"><div class="thumb" role="img" aria-label="Rider wearing number 38 on track" style="background:radial-gradient(#c9a060,#4a4a5a)"></div><div><h4>Ut enim ad minima veniam</h4><p>elit, sed do eiusmod tempor incididunt ut labore et dolore magna aliqua. Ut enim ad minim veniam</p></div></div>
  </div>
</section>

<section class="news">
  <h2 class="title">Latest News</h2>
  <span class="bar"></span>
  <article class="news-card" style="left:126px"><div class="pic" role="img" aria-label="Rider with a red motocross bike under a pit tent" style="background:linear-gradient(135deg,#c9c4c0,#b3282c)"><span class="date">28 MAY 2021</span></div><h4>Lorem ipsum dolor sit amet, consectetur adipiscing elit sed do</h4><div class="more">LEARN MORE <b>→</b></div></article>
  <article class="news-card" style="left:451px"><div class="pic" role="img" aria-label="Race official signalling riders at the start" style="background:linear-gradient(135deg,#7a8a6a,#2d3c66)"><span class="date">28 MAY 2021</span></div><h4>Lorem ipsum dolor sit amet, consectetur adipiscing elit sed do</h4><div class="more">LEARN MORE <b>→</b></div></article>
  <article class="news-card" style="left:776px"><div class="pic" role="img" aria-label="Young rider on a red bike kicking up sand" style="background:linear-gradient(135deg,#b08a5a,#c23a2a)"><span class="date">28 MAY 2021</span></div><h4>Lorem ipsum dolor sit amet, consectetur adipiscing elit sed do</h4><div class="more">LEARN MORE <b>→</b></div></article>
</section>

<section class="testi">
  <h2 class="title">Testimonial</h2>
  <span class="bar"></span>
  <svg class="arrow" style="left:108px" width="24" height="40" viewBox="0 0 24 40"><path d="M20 4L6 20l14 16" stroke="#999" stroke-width="4" fill="none"/></svg>
  <div class="quote" style="left:155px">
    <div class="avatar" role="img" aria-label="Club member portrait" style="background:#c9c9c9"></div>
    “Lorem Ipsum is simply dummy text of the printing and typesetting industry. Lorem Ipsum has been the industry's standard dummy text ever since the 1500s, when an unknown printer stry's standard utry. Lorem Ipsum has been ”
    <span class="by">By Liam</span>
    <svg class="qmark" width="52" height="36" viewBox="0 0 52 36"><path d="M2 2h20v18l-8 14H6l6-14H2zM28 2h20v18l-8 14h-8l6-14h-10z" fill="#ddd"/></svg>
  </div>
  <div class="quote" style="left:619px">
    <div class="avatar" role="img" aria-label="Club member portrait" style="background:#4aa9b0"></div>
    “Lorem Ipsum is simply dummy text of the printing and typesetting industry. Lorem Ipsum has been the industry's standard dummy text ever since the 1500s, when an unknown printer stry's standard utry. Lorem Ipsum has been ”
    <span class="by">By Liam</span>
    <svg class="qmark" width="52" height="36" viewBox="0 0 52 36"><path d="M2 2h20v18l-8 14H6l6-14H2zM28 2h20v18l-8 14h-8l6-14h-10z" fill="#ddd"/></svg>
  </div>
  <svg class="arrow" style="left:1092px" width="24" height="40" viewBox="0 0 24 40"><path d="M4 4l14 16L4 36" stroke="#d3121c" stroke-width="4" fill="none"/></svg>
</section>

<section class="training" role="img" aria-label="Young rider in number 15 gear on a small motocross bike">
  <svg class="train-bg" width="1200" height="499" viewBox="0 0 1200 499"><defs><linearGradient id="tr" x1="0" y1="0" x2="1" y2="1"><stop offset="0" stop-color="#8f0a10"/><stop offset=".5" stop-color="#d3121c"/><stop offset="1" stop-color="#e8242c"/></linearGradient></defs><path d="M0 0H636L460 499H0z" fill="url(#tr)"/></svg>
  <div class="train-text">
    <h2 class="title">Traning &amp; Facilities</h2>
    <span class="bar"></span>
    <p>Lorem ipsum dolor sit amet, consectetur adipiscing elit, sed do eiusmod tempor incididunt ut labore et dolore magna aliqua. Ut enim ad minim veniam, quis nostrud exercitation ullamco laboris nisi ut aliquip ex ea commodo consequat.</p>
    <p>Duis aute irure dolor in voluptate velit esse cillum dolore eu fugiat nulla pariatur. Excepteur sint0</p>
    <span class="btn">LEARN MORE</span>
  </div>
</section>

<section class="latest">
  <h2 class="title">Latest <em>Events</em></h2>
  <span class="bar"></span>
  <div class="photo le-pic" style="left:120px;background:linear-gradient(135deg,#8a9ab0,#2b3350)" role="img" aria-label="Race official waving to riders"></div>
  <div class="photo le-pic" style="left:621px;background:linear-gradient(135deg,#c08a3a,#2d3046)" role="img" aria-label="Rider number 38 on a blue motocross bike"></div>
  <div class="le-card" style="left:145px"><div class="d">20 APR 2022</div><h4>Lorem ipsum dolor sit amet</h4><i></i><p>Lorem ipsum dolor sit amet, consectetur adipiscing elit, sed do eiusmod tempor incididunt ut labore et dolore magna.</p><span>LEARN MORE</span></div>
  <div class="le-card" style="left:648px"><div class="d">20 APR 2022</div><h4>Lorem ipsum dolor sit amet</h4><i></i><p>Lorem ipsum dolor sit amet, consectetur adipiscing elit, sed do eiusmod tempor incididunt ut labore et dolore magna.</p><span>LEARN MORE</span></div>
</section>

<section class="partners">
  <h2 class="title">Our <em>Partners</em></h2>
  <span class="bar"></span>
  <div class="logos" style="top:178px">
    <span style="width:130px;height:22px"></span><span style="width:96px;height:50px"></span><span style="width:120px;height:42px"></span><span style="width:92px;height:44px"></span><span style="width:70px;height:70px;border-radius:50%"></span>
  </div>
  <div class="logos" style="top:300px">
    <span style="width:52px;height:64px"></span><span style="width:150px;height:26px"></span><span style="width:136px;height:32px"></span><span style="width:56px;height:70px"></span><span style="width:166px;height:36px"></span>
  </div>
</section>

<footer class="footer">
  <div class="f-brand"><i></i>SMC</div>
  <div class="socials"><span aria-label="Social link"></span><span aria-label="Social link"></span><span aria-label="Social link"></span><span aria-label="Social link"></span></div>
  <div class="vline" style="left:375px"></div><div class="vline" style="left:645px"></div><div class="vline" style="left:893px"></div>
  <div class="f-col" style="left:399px">
    <h5>NAVIGATION</h5>
    <div class="f-nav"><span>Home</span><span>Calendar</span><span>About Us</span><span>Next Event</span><span>Our Races</span><span>Our Partners</span><span>Facilities</span><span>Links</span><span>Shop</span><span>Contact Us</span></div>
  </div>
  <div class="f-col f-news" style="left:670px;width:200px">
    <h5>LATEST NEWS</h5>
    <p><b>Lorem ipsum dolor sit amet</b>Aonsectetur adipiscing elit, sed do eiusmod tempor incididunt</p>
    <p><b>Sed ut perspiciatis unde</b>Aonsectetur adipiscing elit, sed do eiusmod tempor incididunt</p>
    <p><b>Lorem ipsum dolor sit amet</b>Aonsectetur adipiscing elit, sed do eiusmod tempor incididunt</p>
  </div>
  <div class="f-col f-contact" style="left:911px">
    <h5>CONTACT US</h5>
    <div><span class="ic"><svg width="12" height="14" viewBox="0 0 12 14"><path d="M6 0a5 5 0 0 1 5 5c0 4-5 9-5 9S1 9 1 5a5 5 0 0 1 5-5z" fill="#050505"/><circle cx="6" cy="5" r="2" fill="#fff"/></svg></span><span>48 Dune Road,<br>Saltmarsh Bay 20417</span></div>
    <div><span class="ic"><svg width="14" height="10" viewBox="0 0 14 10"><rect width="14" height="10" rx="1" fill="#050505"/><path d="M1 1l6 5 6-5" stroke="#fff" fill="none"/></svg></span><span>hello@saltmarshmx.com</span></div>
    <div><span class="ic"><svg width="12" height="12" viewBox="0 0 12 12"><path d="M2 1l2 2.5-1 1.3c.7 1.4 1.8 2.5 3.2 3.2l1.3-1L10 9l-1 2C5 10.6 1.4 7 1 3z" fill="#050505"/></svg></span><span style="font-size:12px">(+971) 555 0142</span></div>
  </div>
  <div class="f-rule"></div>
  <div class="copy">© 2021 Saltmarsh Motocross Club | All Rights Reserved</div>
</footer>

</body>
</html>
```